website for LanternPeak Advisory - a HR Consultancy Company

Creation of a website template. I would like to make it with with Wix, but am open to other online website programms.

Website is for consulting company in human resources offering the following services:
- Human resources and talent management for small companies
- Human resources consulting for start-ups
- Diversity and Inclusion management/training
- Board of Directors - talent identification and need evalutation
- coaching and counseling

Pages needed:
- Home page
- HR and talent management
- HR consulting for start-ups
- Diversity & Inclusion management/training
- coaching and counseling
- contact

1. My logo below
2. an example website that I like (not in terms of colours): https://www.mapleridgeadvisors.ch/
http://www.veldorquint.ch/

Target Market(s)

small and mid-sized companies, start-ups

Industry/Entity Type

Consulting

Number of Pages Required

5+ page

Font styles to use
Serif
Sans Serif

Colors
3277b5
35a7d7

Requirements
Must have
• - easy on the eye yet professional looking
• - my text is short
• - website should be clear and easy to understand
Nice to have
• - I will include photographs of the coaches
Should not have
• too many colours
• complicated

```html
<!DOCTYPE html>
<html lang="en">
<head>
<meta charset="utf-8">
<title>LanternPeak Advisory – HR Consulting</title>
<link href="https://fonts.googleapis.com/css2?family=Open+Sans:wght@400;600;700&family=Roboto:wght@400;500&display=swap" rel="stylesheet">
<style>
  :root {
    --brand-blue: #1a70b8;
    --brand-blue-light: #35a7d7;
    --text-dark: #333333;
    --text-body: #555555;
    --text-muted: #6e6e6e;
    --section-grey: #eeeef0;
    --arc-grey: #6b6b6b;
    --footer-bg: #3b3b3b;
    --footer-bottom: #575757;
    --white: #ffffff;
  }
  * { margin: 0; padding: 0; box-sizing: border-box; }
  html, body { width: 1200px; height: 2314px; overflow: hidden; }
  body { position: relative; background: var(--white); font-family: "Roboto", Arial, sans-serif; color: var(--text-body); }
  .abs { position: absolute; }

  /* Header */
  .site-header { left: 0; top: 0; width: 1200px; height: 103px; background: var(--white); }
  .brand-name { left: 134px; top: 30px; font-family: "Open Sans", Arial, sans-serif; font-weight: 700; font-size: 22px; line-height: 26px; color: var(--brand-blue); width: 200px; }
  .call-icon { left: 885px; top: 25px; width: 30px; height: 30px; border-radius: 50%; background: #5d5d5d; }
  .call-label { left: 928px; top: 20px; font-family: "Open Sans", Arial, sans-serif; font-size: 10px; font-weight: 600; color: #666; letter-spacing: .2px; }
  .call-number { left: 928px; top: 33px; font-family: "Open Sans", Arial, sans-serif; font-size: 21px; font-weight: 700; color: var(--brand-blue); }
  .main-nav { left: 582px; top: 69px; height: 34px; display: flex; font-family: "Open Sans", Arial, sans-serif; font-size: 11px; font-weight: 600; color: #444; }
  .main-nav span { padding: 0 16px; line-height: 34px; }
  .main-nav .active { background: var(--brand-blue); color: var(--white); padding: 0 12px; }

  /* Hero */
  .hero { left: 0; top: 103px; width: 1200px; height: 565px; background: linear-gradient(100deg, #b9c3c8 0%, #dde2e4 30%, #c7ced2 55%, #eef0f1 80%, #d9dee1 100%); }
  .hero-title { left: 375px; top: 372px; width: 450px; height: 64px; background: rgba(53,140,210,.75); color: var(--white); font-family: "Open Sans", Arial, sans-serif; font-weight: 700; font-size: 38px; line-height: 64px; text-align: center; }
  .slider-dots { left: 552px; top: 603px; display: flex; gap: 15px; }
  .slider-dots i { width: 12px; height: 12px; border-radius: 50%; background: #5e6266; }
  .slider-dots i.on { background: var(--brand-blue); }

  /* Services */
  .services { left: 0; top: 668px; width: 1200px; height: 514px; background: var(--section-grey); }
  .section-title { width: 1200px; left: 0; text-align: center; font-family: "Open Sans", Arial, sans-serif; font-weight: 700; font-size: 21px; line-height: 28px; color: var(--brand-blue); }
  .title-rule { left: 585px; width: 30px; height: 2px; background: #555; }
  .services-intro { left: 385px; top: 788px; width: 430px; text-align: center; font-size: 13px; line-height: 19px; color: var(--text-body); }
  .arc { left: 0; top: 668px; }
  .service-label { font-size: 12px; line-height: 16px; color: #4a4a4a; text-align: center; }

  /* Welcome */
  .welcome-intro { left: 131px; top: 1255px; width: 345px; font-size: 13px; line-height: 20px; color: var(--text-muted); text-align: justify; }
  .feature-icon { left: 131px; }
  .feature-title { left: 185px; font-family: "Open Sans", Arial, sans-serif; font-size: 12px; font-weight: 600; color: #3a3a3a; }
  .feature-text { left: 185px; width: 278px; font-size: 12px; line-height: 18px; color: var(--text-muted); text-align: justify; }
  .welcome-photo { left: 543px; top: 1245px; width: 524px; height: 348px; background: linear-gradient(110deg, #e9e6e2 0%, #d7d2cc 45%, #c9cfd6 75%, #ebe4d6 100%); }

  /* HR band */
  .hr-band { left: 0; top: 1661px; width: 1200px; height: 446px; background: linear-gradient(90deg, #dfe7ee 0%, #cfdae4 40%, #e4e9ee 70%, #c9d2da 100%); }
  .hr-title { left: 221px; top: 1740px; font-family: "Roboto", Arial, sans-serif; font-weight: 500; font-size: 28px; color: var(--brand-blue); }
  .hr-text { left: 221px; top: 1797px; width: 352px; font-size: 13px; line-height: 21px; color: #4a4a4a; text-align: justify; }
  .btn-contact { left: 222px; top: 1886px; width: 145px; height: 39px; background: var(--brand-blue); color: var(--white); font-family: "Open Sans", Arial, sans-serif; font-size: 15px; font-weight: 600; text-align: center; line-height: 39px; }

  /* Footer */
  .site-footer { left: 0; top: 2107px; width: 1200px; height: 177px; background: var(--footer-bg); }
  .footer-brand { left: 134px; top: 2170px; width: 210px; font-family: "Open Sans", Arial, sans-serif; font-weight: 700; font-size: 22px; line-height: 26px; color: var(--white); }
  .footer-heading { font-family: "Open Sans", Arial, sans-serif; font-size: 12px; font-weight: 700; color: var(--white); }
  .footer-menu { left: 381px; top: 2176px; font-size: 10px; color: #e8e8e8; letter-spacing: .2px; }
  .social { left: 466px; top: 2211px; display: flex; gap: 9px; }
  .social i { width: 24px; height: 24px; border-radius: 50%; background: #2f78c8; }
  .newsletter-input { left: 808px; top: 2187px; width: 261px; height: 51px; background: var(--white); }
  .newsletter-input span { position: absolute; left: 17px; top: 18px; font-size: 10px; color: #444; }
  .copyright-bar { left: 0; top: 2284px; width: 1200px; height: 30px; background: var(--footer-bottom); color: #e2e2e2; font-size: 10px; text-align: center; line-height: 30px; }
</style>
</head>
<body>

<header class="abs site-header"></header>
<div class="abs brand-name">LanternPeak Advisory</div>
<div class="abs call-icon">
  <svg width="30" height="30" viewBox="0 0 30 30"><path d="M11 9c1 0 2 2.5 2 3s-1 1-1 1.7c.6 1.6 2 3 3.5 3.6.7 0 1.2-1 1.7-1s3 1 3 2-1.3 2.4-2.5 2.4C13 20.7 9.3 17 9 11.3 9 10 10 9 11 9z" fill="#fff"/></svg>
</div>
<div class="abs call-label">CALL US NOW ON</div>
<div class="abs call-number">555.010.4821</div>
<nav class="abs main-nav">
  <span class="active">HOME</span><span>ABOUT US</span><span>SERVICES</span><span>CONSULTING</span><span>BLOG</span><span>CONTACT US</span>
</nav>

<section class="abs hero" role="img" aria-label="Photo of a team of consultants working at laptops around a meeting table"></section>
<h1 class="abs hero-title">CONSULTING SERVICES</h1>
<div class="abs slider-dots"><i></i><i></i><i class="on"></i><i></i><i></i></div>

<section class="abs services"></section>
<h2 class="abs section-title" style="top:712px">OUR SERVICES</h2>
<div class="abs title-rule" style="top:748px"></div>
<p class="abs services-intro">There are many variations of passages of Lorem Ipsum available, but the majority have suffered a alteration in some form by injected</p>

<svg class="abs arc" width="1200" height="514" viewBox="0 0 1200 514">
  <path d="M281 514 C 360 300, 500 290, 598 290 C 700 290, 840 300, 921 514 C 830 350, 700 336, 598 336 C 496 336, 372 350, 281 514 Z" fill="var(--arc-grey)"/>
  <g fill="var(--arc-grey)" stroke="var(--section-grey)" stroke-width="5">
    <circle cx="361" cy="402" r="38"/>
    <circle cx="466" cy="325" r="38"/>
    <circle cx="598" cy="304" r="38"/>
    <circle cx="753" cy="329" r="38"/>
    <circle cx="850" cy="405" r="38"/>
  </g>
  <g fill="none" stroke="#fff" stroke-width="2">
    <circle cx="361" cy="399" r="11"/><circle cx="361" cy="396" r="3" fill="#fff"/><path d="M355 406 q6-6 12 0"/>
    <rect x="452" y="318" width="28" height="10"/><path d="M456 328v8M476 328v8M466 313v5"/>
    <path d="M598 290v10M586 300h24M586 300v8M598 300v8M610 300v8"/><rect x="594" y="285" width="8" height="6" fill="#fff"/>
    <rect x="740" y="320" width="26" height="18" rx="2"/><path d="M746 326h6M746 331h14"/>
    <path d="M850 391v28M836 405h28M840 395l20 20M860 395l-20 20"/>
  </g>
</svg>
<div class="abs service-label" style="left:188px;top:1007px;width:140px">Human resources and talent management for small companies</div>
<div class="abs service-label" style="left:302px;top:924px;width:140px">Human resources consulting for start-ups</div>
<div class="abs service-label" style="left:525px;top:882px;width:160px">Diversity and Inclusion management/training</div>
<div class="abs service-label" style="left:752px;top:915px;width:150px">Board of Directors - talent identification and need evaluation</div>
<div class="abs service-label" style="left:882px;top:1030px;width:100px">coaching and counseling</div>

<h2 class="abs section-title" style="top:1143px">WELCOME TO OUR SITE</h2>
<div class="abs title-rule" style="top:1190px"></div>

<p class="abs welcome-intro">There are many variations of passages of Lorem Ipsum available, but the majority have suffered.</p>

<svg class="abs feature-icon" style="top:1334px" width="28" height="24" viewBox="0 0 28 24"><path d="M2 11 L26 2 L19 22 L13 14 Z M13 14 L26 2" fill="none" stroke="#555" stroke-width="2" stroke-linejoin="round"/></svg>
<div class="abs feature-title" style="top:1331px">MISSION &amp; VISION</div>
<p class="abs feature-text" style="top:1355px">But the majority have suffered alteration in some form, by injected humour.</p>

<svg class="abs feature-icon" style="top:1428px" width="28" height="24" viewBox="0 0 28 24"><circle cx="10" cy="7" r="5" fill="#555"/><circle cx="19" cy="8" r="4" fill="#555"/><path d="M1 22c0-7 18-7 18 0z M17 22c1-5 10-6 10 0z" fill="#555"/></svg>
<div class="abs feature-title" style="top:1424px">TEAM</div>
<p class="abs feature-text" style="top:1448px">But the majority have suffered alteration in some form, by injected humour.</p>

<svg class="abs feature-icon" style="top:1519px" width="28" height="24" viewBox="0 0 28 24"><path d="M4 3h18a3 3 0 0 1 3 3v9a3 3 0 0 1-3 3H11l-6 5v-5H4a3 3 0 0 1-3-3V6a3 3 0 0 1 3-3z" fill="#555"/><circle cx="8" cy="11" r="1.6" fill="#fff"/><circle cx="13" cy="11" r="1.6" fill="#fff"/><circle cx="18" cy="11" r="1.6" fill="#fff"/></svg>
<div class="abs feature-title" style="top:1517px">CONSULTING</div>
<p class="abs feature-text" style="top:1541px">But the majority have suffered alteration in some form, by injected humour.</p>

<div class="abs welcome-photo" role="img" aria-label="Photo of a smiling consultant in a coaching conversation with a client in a bright office"></div>

<section class="abs hr-band" role="img" aria-label="Photo of a businessman working on a laptop in a bright office with large windows"></section>
<h2 class="abs hr-title">Human Resources</h2>
<p class="abs hr-text">There are many variations of passages of Lorem Ipsum available, but the majority have suffered alteration in some form, by injected humour, or randomised</p>
<div class="abs btn-contact">CONTACT US</div>

<footer class="abs site-footer"></footer>
<div class="abs footer-brand">LanternPeak Advisory</div>
<div class="abs footer-heading" style="left:381px;top:2152px">MENU</div>
<div class="abs footer-menu">HOME &nbsp;|&nbsp; ABOUT US &nbsp;|&nbsp; SERVICES &nbsp;|&nbsp; CONSULTING &nbsp;|&nbsp; BLOG &nbsp;|&nbsp; CONTACT US</div>
<div class="abs footer-heading" style="left:381px;top:2215px">FOLOW US</div>
<div class="abs social"><i></i><i></i><i style="background:#3b5ac0"></i></div>
<div class="abs footer-heading" style="left:807px;top:2152px">NEWSLETTER</div>
<div class="abs newsletter-input">
  <span>E MAIL ID</span>
  <svg style="position:absolute;left:222px;top:19px" width="24" height="12" viewBox="0 0 24 12"><path d="M0 6h21M16 1l5 5-5 5" fill="none" stroke="#222" stroke-width="2"/></svg>
</div>
<div class="abs copyright-bar">Copyrights @ 2017 All Rights Reserved</div>

</body>
</html>
```